" A empresa é afiliada a Vantrel Investimentos e atua com produtos financeiros de investimentos: Fundos, Aplicaçoes de Renda Fixa, Açoes, Mercado Futuro e Derivativos. "

```html
<!DOCTYPE html>
<html lang="pt-BR">
<head>
<meta charset="utf-8">
<title>Assinatura de e-mail – Quorvela</title>
<link rel="stylesheet" href="https://fonts.googleapis.com/css2?family=Open+Sans:wght@300;400;600&display=swap">
<style>
  :root {
    --page-bg: #e9e9e9;
    --card-bg: #ffffff;
    --ink-dark: #3a3a3a;
    --ink-mid: #5c5c5c;
    --ink-soft: #8a8a8a;
    --brand-blue: #2f6fa8;
    --partner-bg: #3b3b3b;
    --partner-ink: #ffffff;
    --divider: #c9c9c9;
  }
  * { margin: 0; padding: 0; box-sizing: border-box; }
  html, body {
    width: 1200px; height: 1200px; overflow: hidden;
    background: var(--page-bg);
    font-family: "Open Sans", Arial, sans-serif;
  }
  .canvas {
    width: 1200px; height: 1200px;
    display: flex; align-items: center; justify-content: center;
  }
  .signature {
    width: 1000px; height: 390px;
    background: var(--card-bg);
    display: flex;
    box-shadow: 0 6px 24px rgba(0,0,0,0.12);
  }
  .brand-column {
    width: 400px;
    display: flex; flex-direction: column;
  }
  .brand-agency {
    flex: 1;
    display: flex; align-items: center; gap: 18px;
    padding: 0 34px;
  }
  .brand-mark {
    width: 70px; height: 70px; border-radius: 50%;
    background: var(--brand-blue);
    flex: none;
  }
  .brand-name {
    font-size: 46px; font-weight: 400; letter-spacing: 3px;
    color: var(--brand-blue); line-height: 1;
  }
  .brand-tagline {
    margin-top: 8px;
    font-size: 11px; letter-spacing: 1px;
    color: var(--brand-blue); text-transform: uppercase;
  }
  .brand-partner {
    height: 160px;
    background: var(--partner-bg);
    color: var(--partner-ink);
    display: flex; flex-direction: column; justify-content: center;
    padding: 0 34px;
  }
  .partner-intro {
    font-size: 15px; font-weight: 300; font-style: normal;
  }
  .partner-name {
    margin-top: 8px;
    font-size: 38px; font-weight: 300; line-height: 1;
    display: flex; align-items: center; gap: 12px;
  }
  .partner-dot {
    width: 22px; height: 22px; background: var(--partner-ink);
  }
  .partner-note {
    margin-top: 10px; font-size: 10px; letter-spacing: 1px;
    text-transform: uppercase; opacity: 0.8;
  }
  .divider { width: 1px; background: var(--divider); margin: 30px 0; }
  .contact-column {
    flex: 1;
    padding: 46px 40px;
    display: flex; flex-direction: column;
  }
  .person-name {
    font-size: 36px; font-weight: 400; color: var(--ink-dark);
  }
  .person-role {
    margin-top: 4px; font-size: 17px; color: var(--ink-mid);
  }
  .contact-lines {
    margin-top: 34px;
    font-size: 16px; line-height: 1.6; color: var(--ink-mid);
  }
  .contact-lines .address { margin-top: 12px; }
</style>
</head>
<body>
<main class="canvas">
  <section class="signature" aria-label="Assinatura de e-mail">
    <div class="brand-column">
      <div class="brand-agency">
        <span class="brand-mark"></span>
        <div>
          <div class="brand-name">QUORVELA</div>
          <div class="brand-tagline">Agentes Autônomos de Investimento</div>
        </div>
      </div>
      <div class="brand-partner">
        <div class="partner-intro">um agente de investimento da</div>
        <div class="partner-name"><span class="partner-dot"></span>Vantrel Investimentos</div>
        <div class="partner-note">Credenciado nº 000.000</div>
      </div>
    </div>
    <div class="divider"></div>
    <div class="contact-column">
      <div class="person-name">Helena Sobrenome Completo</div>
      <div class="person-role">Quorvela - Agentes Autônomos de Investimento</div>
      <div class="contact-lines">
        <div>(11) 5550-0147 | helena@quorvelainvest.com.br</div>
        <div>www.quorvelainvestimentos.com.br</div>
        <div class="address">R. Alameda das Acácias, 415 cj 82</div>
        <div>Jardim Aurora - São Paulo SP - CEP 01455-000</div>
      </div>
    </div>
  </section>
</main>
</body>
</html>
```